Graphic Design for an online custom wine label company

Provides artistic and funky wine labels to people online. People can customize the text on the label.

```html
<!DOCTYPE html>
<html lang="en">
<head>
<meta charset="utf-8">
<title>Wine Label</title>
<link rel="stylesheet" href="https://fonts.googleapis.com/css2?family=Yellowtail&family=Questrial&display=swap">
<style>
  :root {
    --bg: #000000;
    --frame-brown: #7a4e2a;
    --frame-grey: #a9a9a9;
    --label-tan: #c49a5a;
    --ink-white: #ffffff;
    --mascot-light: #86dcd3;
    --mascot-mid: #5fb8b0;
  }
  html, body {
    margin: 0;
    padding: 0;
    width: 900px;
    height: 1200px;
    overflow: hidden;
    background: var(--bg);
  }
  .label-canvas {
    position: relative;
    width: 900px;
    height: 1200px;
    background: var(--bg);
    overflow: hidden;
  }
  .label-art {
    position: absolute;
    inset: 0;
  }
  .label-text {
    position: absolute;
    left: 0;
    width: 900px;
    margin: 0;
    text-align: center;
    color: var(--ink-white);
    white-space: nowrap;
  }
  .wine-name {
    font-family: "Yellowtail", "Brush Script MT", cursive;
    font-weight: 400;
    font-size: 176px;
    line-height: 176px;
    height: 176px;
    transform: rotate(-5deg);
  }
  .wine-name--first {
    top: 590px;
    left: -56px;
  }
  .wine-name--second {
    top: 712px;
    left: 78px;
  }
  .wine-description {
    top: 900px;
    font-family: "Questrial", sans-serif;
    font-size: 66px;
    line-height: 66px;
    height: 66px;
  }
  .wine-subline {
    top: 976px;
    height: 34px;
    display: flex;
    justify-content: center;
    align-items: center;
    gap: 14px;
  }
  .wine-subline__rule {
    width: 104px;
    height: 4px;
    border-top: 3px solid var(--ink-white);
    border-bottom: 3px solid var(--ink-white);
  }
  .wine-subline__text {
    font-family: "Questrial", sans-serif;
    font-size: 32px;
    line-height: 34px;
  }
  .label-foot {
    position: absolute;
    top: 1023px;
    margin: 0;
    font-family: "Questrial", sans-serif;
    font-size: 21px;
    line-height: 24px;
    color: var(--ink-white);
    white-space: nowrap;
  }
  .label-foot--volume { left: 236px; }
  .label-foot--origin { left: 545px; }
</style>
</head>
<body>
<main class="label-canvas">
  <svg class="label-art" width="900" height="1200" viewBox="0 0 900 1200" xmlns="http://www.w3.org/2000/svg">
    <defs>
      <linearGradient id="mascot-tone" x1="0" y1="0" x2="1" y2="1">
        <stop offset="0" stop-color="var(--mascot-light)"/>
        <stop offset="1" stop-color="var(--mascot-mid)"/>
      </linearGradient>
      <path id="badge-shape" d="M130,575 Q450,545 770,575 Q790,632 843,642 Q862,830 800,990 Q770,1000 760,1040 Q450,1140 140,1040 Q130,1000 100,990 Q38,830 57,642 Q110,632 130,575 Z"/>
    </defs>

    <rect class="mascot-illustration" role="img"
          aria-label="Cartoon mascot: a smiling spotted teal cow leaning on the label, raising a red cocktail glass with little red hearts floating above"
          x="95" y="110" width="535" height="500" rx="90" ry="90"
          fill="url(#mascot-tone)"/>

    <g class="badge">
      <use href="#badge-shape" fill="var(--frame-brown)"/>
      <use href="#badge-shape" fill="var(--frame-grey)" transform="translate(450 840) scale(0.95) translate(-450 -840)"/>
      <use href="#badge-shape" fill="var(--label-tan)" transform="translate(450 840) scale(0.93) translate(-450 -840)"/>
    </g>
  </svg>

  <h1 class="label-text wine-name wine-name--first">Wine</h1>
  <p class="label-text wine-name wine-name--second">Name</p>
  <p class="label-text wine-description">Wine Description</p>
  <div class="label-text wine-subline">
    <span class="wine-subline__rule"></span>
    <span class="wine-subline__text">Wine Description</span>
    <span class="wine-subline__rule"></span>
  </div>
  <p class="label-foot label-foot--volume">xxx ml</p>
  <p class="label-foot label-foot--origin">product from</p>
</main>
</body>
</html>
```